Business Card Design

We would like a business card that utilizes our current logo and keeps with the same feel - elegant and organic. Our farm isn't about mass production, it's about excellence, education, beautiful events and flowers - people, culture, and community.

Target Market(s)

Patrons to our farm who are interested in weddings, events, or our flowers and vegetables.

Contact Information for Business Card

Name, address, cell email (Danielle Hoskins, 2716 Wrenfield Rd, Alder Springs, CO 80544, cell 30.412.6638, email danielle@wrenfieldacres.com)

```html
<!DOCTYPE html>
<html lang="en">
<head>
<meta charset="utf-8">
<title>Wrenfield Acres – Business Card</title>
<link href="https://fonts.googleapis.com/css2?family=Cormorant+Garamond:wght@500&family=Arimo:wght@400&display=swap" rel="stylesheet">
<style>
  :root {
    --page-bg: #ecebe7;
    --card-white: #ffffff;
    --sage-light: #8aa898;
    --sage: #6a8a76;
    --sage-deep: #3f5a49;
    --sage-ink: #5d7d6a;
    --text-light: #f4f7f4;
    --divider: #f4f7f4;
  }
  * { box-sizing: border-box; margin: 0; padding: 0; }
  html, body {
    width: 1200px; height: 960px; overflow: hidden;
    background: var(--page-bg);
  }
  .sheet {
    width: 1200px; height: 960px;
    display: flex; flex-direction: column;
    align-items: center; justify-content: center; gap: 56px;
  }
  .card {
    width: 700px; height: 400px;
    border-radius: 4px;
    position: relative; overflow: hidden;
    box-shadow: 0 6px 18px rgba(0,0,0,0.12);
  }

  /* Front */
  .card-front { background: var(--card-white); }
  .front-wordmark {
    position: absolute; right: 60px; top: 118px;
    font-family: "Cormorant Garamond", serif;
    font-weight: 500; font-size: 46px;
    color: var(--sage-ink);
    display: flex; align-items: center; gap: 14px;
  }
  .wordmark-dot {
    width: 12px; height: 12px; border-radius: 50%;
    background: var(--sage-ink);
  }
  .contact-band {
    position: absolute; left: 0; right: 0; bottom: 0; height: 170px;
    background: linear-gradient(100deg, var(--sage) 0%, var(--sage-light) 30%, var(--sage) 65%, var(--sage-deep) 100%);
    display: flex; align-items: center;
    padding: 0 36px 0 40px;
  }
  .person-name {
    font-family: "Cormorant Garamond", serif;
    font-weight: 500; font-size: 34px; letter-spacing: 1px;
    color: var(--text-light);
    width: 280px; flex: none; white-space: nowrap;
  }
  .band-divider {
    width: 2px; height: 112px; background: var(--divider);
    margin-right: 32px; flex: none;
  }
  .contact-list {
    font-family: "Arimo", sans-serif; font-size: 18px; line-height: 1.4;
    color: var(--text-light); list-style: none; white-space: nowrap;
  }
  .contact-list li { display: flex; align-items: center; gap: 10px; }
  .contact-list .address-line { padding-left: 30px; }
  .contact-icon { width: 20px; height: 20px; flex: none; }

  /* Back */
  .card-back {
    background: radial-gradient(ellipse at 25% 20%, var(--sage-light) 0%, var(--sage) 45%, var(--sage-deep) 100%);
    display: flex; align-items: center; justify-content: center;
  }
  .back-wordmark {
    font-family: "Cormorant Garamond", serif;
    font-weight: 500; font-size: 58px;
    color: var(--sage-deep);
    display: flex; align-items: center; gap: 16px;
  }
  .back-wordmark .wordmark-dot { background: var(--sage-deep); width: 14px; height: 14px; }
</style>
</head>
<body>
<main class="sheet">
  <section class="card card-back" aria-label="Card back">
    <div class="back-wordmark"><span class="wordmark-dot"></span>Wrenfield Acres</div>
  </section>

  <section class="card card-front" aria-label="Card front">
    <div class="front-wordmark"><span class="wordmark-dot"></span>Wrenfield Acres</div>
    <div class="contact-band">
      <p class="person-name">Danielle Hoskins</p>
      <span class="band-divider"></span>
      <ul class="contact-list">
        <li class="address-line">2716 Wrenfield Rd</li>
        <li class="address-line">Alder Springs, CO 80544</li>
        <li>
          <svg class="contact-icon" viewBox="0 0 20 20" fill="none" stroke="currentColor" stroke-width="1.5"><rect x="5" y="1.5" width="10" height="17" rx="1.8"/><line x1="8.5" y1="15.5" x2="11.5" y2="15.5"/></svg>
          30.412.6638
        </li>
        <li>
          <svg class="contact-icon" viewBox="0 0 20 20" fill="none" stroke="currentColor" stroke-width="1.5"><rect x="1.5" y="4.5" width="17" height="11"/><polyline points="1.5,4.5 10,11 18.5,4.5"/></svg>
          danielle@wrenfieldacres.com
        </li>
      </ul>
    </div>
  </section>
</main>
</body>
</html>
```